Wendale Information Posters for Student signage

Secondary school looking for some posters to display throughout the school with fresh designs using school colours and fitting with general feel of the school's graphic image. The final designs should be welcoming but clearly outline the required instructions. Sample designs that have been created by the school are attached with the relevant information that is required to appear on the signs. School would like a more dynamic design than the basic signs attached.
We are looking for:
- Large pop-up banner style size for the 2 posters called
"Ready for class" and "Morning Routine".
- Printable poster for the "Wendale Outdoor" sign.

Please incorporate a design feature of "the Wendale 1,2,3" into the posters and also use the Wendale Leaner values of Integrity, Compassion, Curiosity and Drive to help illustrate the content.

An option for design is to incorporate our school's first nations artwork into the design and i have also provided various extracts of design pieces that the school often uses in it's marketing materials.

Target Market(s)

Secondary School Students

Industry/Entity Type

Education

Colors
00AB8E
00BBA5
67D7C9
C6EFE9
E9F9F6
FFF300
FFF600
FEFA6F
FFFEC7
FFFEE8
FFC000
F8CF3A
FAE287
FDF2CF
FEFAEE

Requirements
Must have
• My project must have eyecatching graphics

```html
<!DOCTYPE html>
<html lang="en">
<head>
<meta charset="utf-8">
<title>Wendale Student Signage Posters</title>
<link rel="stylesheet" href="https://fonts.googleapis.com/css2?family=Anton&family=Roboto:wght@400;500;700&display=swap">
<style>
  :root{
    --green-dark:#1d4a2a;
    --green-photo:#2f7a4f;
    --green-deep:#1c5a36;
    --yellow:#f5c400;
    --cream:#f4efe6;
    --line:#1d4a2a;
    --muted:#7a9a6a;
    --page:#ffffff;
  }
  *{box-sizing:border-box;margin:0;padding:0}
  html,body{width:1200px;height:738px;overflow:hidden;background:var(--page)}
  .canvas{position:relative;width:1200px;height:738px}
  .poster{position:absolute;top:85px;width:380px;height:568px;background:var(--cream);overflow:hidden;box-shadow:3px 3px 4px rgba(0,0,0,.35);font-family:"Roboto",sans-serif;color:var(--green-dark)}
  .poster--hats{left:13px}
  .poster--ready{left:411px}
  .poster--morning{left:810px}
  .photo{position:absolute;left:0;top:0}
  .artwork{position:absolute;left:72px;top:25px;width:76px;height:76px;border-radius:50%;background:radial-gradient(circle,#f5c400 0 8%,#6c7a3a 30%,#1a2a14 70%,#0d160b 100%)}
  .brand{position:absolute;right:20px;top:40px;display:flex;align-items:center;gap:5px;font-family:"Anton",sans-serif;font-size:15px;color:var(--green-dark);letter-spacing:.5px}
  .brand-dot{width:12px;height:12px;border-radius:50%;background:var(--yellow)}
  .title{position:absolute;left:147px;top:94px;font-family:"Anton",sans-serif;font-size:50px;line-height:50px;text-transform:uppercase;color:var(--green-dark);letter-spacing:.5px}
  .num{position:absolute;font-family:"Anton",sans-serif;color:var(--yellow);line-height:1}
  .divider{position:absolute;width:1px;background:#b9b9a8}
  .rule{position:absolute;height:1px;background:#9aa790}
  .label{position:absolute;font-family:"Anton",sans-serif;font-size:24px;color:var(--green-dark);letter-spacing:.3px}
  .step-text{position:absolute;font-size:13px;line-height:17px;color:var(--green-dark)}
  .step-text small{font-size:9.5px}
  .step-text--sm{font-size:10.5px;line-height:13px}
  .icon-fill{position:absolute;left:198px;width:52px;height:52px;border-radius:6px;background:linear-gradient(135deg,#8aa465,#3d6a3a)}
  .icon{position:absolute}
  .connector{position:absolute;width:1px;background:var(--green-dark)}
  .connector::after{content:"";position:absolute;left:-3px;bottom:-3px;width:7px;height:7px;border-radius:50%;background:var(--yellow);border:1px solid var(--green-dark)}
  .col-head{position:absolute;top:212px;font-family:"Anton",sans-serif;font-size:13px;color:var(--green-dark);letter-spacing:.3px;padding-bottom:6px;border-bottom:1px solid var(--green-dark);width:58px;white-space:nowrap}
  .footer{position:absolute;left:147px;top:526px;width:205px;border-top:1px solid var(--line);padding-top:5px}
  .footer-value{font-weight:700;font-size:10.5px;letter-spacing:2px;color:var(--green-dark)}
  .footer-sub{font-size:7px;letter-spacing:2px;color:var(--muted);margin-top:3px}
</style>
</head>
<body>
<div class="canvas">

  <!-- Poster: hats -->
  <section class="poster poster--hats">
    <svg class="photo" width="380" height="568" role="img" aria-label="Green-tinted photo of students running up outdoor stairs">
      <defs><linearGradient id="g1" x1="0" y1="0" x2="0" y2="1"><stop offset="0" stop-color="#3a7e55"/><stop offset=".55" stop-color="#2c6a45"/><stop offset="1" stop-color="#1f4f33"/></linearGradient></defs>
      <polygon points="0,0 107,0 136,568 0,568" fill="url(#g1)"/>
    </svg>
    <div class="artwork" role="img" aria-label="First Nations dot artwork circle"></div>
    <div class="brand"><span class="brand-dot"></span>WENDALE</div>
    <h1 class="title">We wear<br>hats at<br>Wendale</h1>

    <span class="num" style="left:148px;top:264px;font-size:56px">1</span>
    <span class="divider" style="left:185px;top:268px;height:48px"></span>
    <div class="icon-fill" style="top:266px" role="img" aria-label="Student in bucket hat illustration"></div>
    <span class="label" style="left:264px;top:272px">WALKING</span>
    <span class="rule" style="left:148px;top:334px;width:204px"></span>

    <span class="num" style="left:148px;top:362px;font-size:56px">2</span>
    <span class="divider" style="left:185px;top:366px;height:48px"></span>
    <div class="icon-fill" style="top:362px" role="img" aria-label="Student sitting in hat illustration"></div>
    <span class="label" style="left:264px;top:371px">SITTING</span>
    <span class="rule" style="left:148px;top:430px;width:204px"></span>

    <span class="num" style="left:148px;top:458px;font-size:56px">3</span>
    <span class="divider" style="left:185px;top:462px;height:48px"></span>
    <div class="icon-fill" style="top:458px" role="img" aria-label="Student playing guitar in hat illustration"></div>
    <span class="label" style="left:264px;top:467px">PLAYING</span>

    <div class="footer"><div class="footer-value">INTEGRITY</div><div class="footer-sub">WENDALE LEARNER VALUES</div></div>
  </section>

  <!-- Poster: ready for class -->
  <section class="poster poster--ready">
    <svg class="photo" width="380" height="568" role="img" aria-label="Green-tinted photo of students walking down stairs">
      <defs><linearGradient id="g2" x1="0" y1="0" x2="0" y2="1"><stop offset="0" stop-color="#3e9a5e"/><stop offset=".5" stop-color="#2c6e46"/><stop offset="1" stop-color="#1c4a30"/></linearGradient></defs>
      <polygon points="0,0 107,0 136,568 0,568" fill="url(#g2)"/>
    </svg>
    <div class="artwork" style="top:28px" role="img" aria-label="First Nations dot artwork circle"></div>
    <div class="brand"><span class="brand-dot"></span>WENDALE</div>
    <h1 class="title">Are you<br>ready for<br>class?</h1>

    <span class="num" style="left:148px;top:262px;font-size:56px">1</span>
    <span class="divider" style="left:185px;top:265px;height:48px"></span>
    <svg class="icon" style="left:197px;top:264px" width="58" height="48" viewBox="0 0 58 48" aria-hidden="true">
      <rect x="5" y="2" width="48" height="34" rx="3" fill="none" stroke="#1d4a2a" stroke-width="1.6"/>
      <path d="M1 40 H57 L54 45 H4 Z" fill="none" stroke="#1d4a2a" stroke-width="1.6"/>
      <path d="M14 8 Q21 6 29 9 Q37 6 44 8 V30 Q37 28 29 31 Q21 28 14 30 Z" fill="#8aa465" stroke="#1d4a2a" stroke-width="1.2"/>
      <line x1="29" y1="9" x2="29" y2="31" stroke="#1d4a2a" stroke-width="1.2"/>
    </svg>
    <div class="step-text" style="left:275px;top:273px">Laptop /<br>Workbook</div>
    <span class="connector" style="left:165px;top:329px;height:18px"></span>

    <span class="num" style="left:148px;top:360px;font-size:56px">2</span>
    <span class="divider" style="left:185px;top:363px;height:48px"></span>
    <svg class="icon" style="left:212px;top:362px" width="40" height="50" viewBox="0 0 40 50" aria-hidden="true">
      <path d="M2 10 H38 V42 L20 48 L2 42 Z" fill="none" stroke="#1d4a2a" stroke-width="1.6"/>
      <path d="M6 14 H34 V39 L20 44 L6 39 Z" fill="none" stroke="#1d4a2a" stroke-width="1" stroke-dasharray="2 2"/>
      <rect x="14" y="1" width="20" height="11" rx="2" fill="#8aa465" stroke="#1d4a2a" stroke-width="1.4" transform="rotate(8 24 6)"/>
    </svg>
    <div class="step-text" style="left:275px;top:369px">Phone<br>in Pocketa</div>
    <span class="connector" style="left:165px;top:425px;height:21px"></span>

    <span class="num" style="left:148px;top:458px;font-size:56px">3</span>
    <span class="divider" style="left:185px;top:461px;height:48px"></span>
    <svg class="icon" style="left:210px;top:454px" width="40" height="60" viewBox="0 0 40 60" aria-hidden="true">
      <path d="M12 8 Q12 1 20 1 Q28 1 28 8 H33 V11 H7 V8 Z" fill="#1d4a2a"/>
      <path d="M13 17 L4 21 L1 35 L7 36 L9 27 V58 H31 V27 L33 36 L39 35 L36 21 L27 17 L20 24 Z" fill="none" stroke="#1d4a2a" stroke-width="1.5"/>
      <line x1="20" y1="24" x2="20" y2="58" stroke="#1d4a2a" stroke-width="1" stroke-dasharray="2 3"/>
    </svg>
    <div class="step-text" style="left:275px;top:466px">Correct<br>Uniform<br><small>(including hat)</small></div>

    <div class="footer" style="width:190px"><div class="footer-value">INTEGRITY</div><div class="footer-sub">WENDALE LEARNER VALUES</div></div>
  </section>

  <!-- Poster: morning routine -->
  <section class="poster poster--morning">
    <svg class="photo" width="380" height="568" role="img" aria-label="Green-tinted photo of students walking along a school corridor">
      <defs><linearGradient id="g3" x1="0" y1="0" x2="0" y2="1"><stop offset="0" stop-color="#2f6e4c"/><stop offset=".5" stop-color="#2a6546"/><stop offset="1" stop-color="#3a7a58"/></linearGradient></defs>
      <polygon points="0,0 107,0 136,568 0,568" fill="url(#g3)"/>
    </svg>
    <div class="artwork" style="left:67px;top:22px;width:84px;height:84px" role="img" aria-label="First Nations dot artwork circle"></div>
    <div class="brand"><span class="brand-dot"></span>WENDALE</div>
    <h1 class="title">Morning<br>routine</h1>

    <span class="col-head" style="left:147px">ON TIME</span>
    <span class="col-head" style="left:272px">RUNNING LATE</span>

    <!-- on time -->
    <span class="num" style="left:147px;top:255px;font-size:44px">1</span>
    <span class="divider" style="left:177px;top:258px;height:38px"></span>
    <svg class="icon" style="left:193px;top:252px" width="32" height="32" viewBox="0 0 32 32" aria-hidden="true">
      <path d="M28 16 A12 12 0 1 1 20 4.7" fill="none" stroke="#1d4a2a" stroke-width="1.8"/>
      <path d="M22 5 A12 12 0 0 1 28 14" fill="none" stroke="#f5c400" stroke-width="1.8" stroke-dasharray="2 2"/>
      <path d="M16 9 V16 L21 19" fill="none" stroke="#1d4a2a" stroke-width="1.8"/>
    </svg>
    <div class="step-text step-text--sm" style="left:186px;top:290px">Arrive before<br>8:30 AM</div>
    <span class="connector" style="left:176px;top:317px;height:21px"></span>

    <span class="num" style="left:147px;top:357px;font-size:44px">2</span>
    <span class="divider" style="left:177px;top:360px;height:38px"></span>
    <svg class="icon lockers" style="left:194px;top:351px" width="36" height="30" viewBox="0 0 36 30" aria-hidden="true">
      <rect x="1" y="1" width="34" height="28" fill="none" stroke="#1d4a2a" stroke-width="1.4"/>
      <line x1="18" y1="1" x2="18" y2="29" stroke="#1d4a2a" stroke-width="1.2"/>
      <line x1="1" y1="14" x2="35" y2="14" stroke="#1d4a2a" stroke-width="1.2"/>
      <rect x="22" y="18" width="9" height="8" fill="none" stroke="#1d4a2a" stroke-width="1.2"/>
      <circle cx="6" cy="19" r="1.5" fill="#f5c400"/><circle cx="6" cy="6" r="1.5" fill="#f5c400"/>
    </svg>
    <div class="step-text step-text--sm" style="left:186px;top:386px">Place bag<br>in locker</div>
    <span class="connector" style="left:176px;top:421px;height:21px"></span>

    <span class="num" style="left:147px;top:461px;font-size:44px">3</span>
    <span class="divider" style="left:177px;top:464px;height:38px"></span>
    <svg class="icon" style="left:194px;top:463px" width="40" height="22" viewBox="0 0 40 22" aria-hidden="true">
      <circle cx="20" cy="5" r="4" fill="none" stroke="#1d4a2a" stroke-width="1.4"/>
      <circle cx="8" cy="8" r="3.3" fill="none" stroke="#1d4a2a" stroke-width="1.4"/>
      <circle cx="32" cy="8" r="3.3" fill="none" stroke="#1d4a2a" stroke-width="1.4"/>
      <path d="M12 21 Q12 11 20 11 Q28 11 28 21 M1 21 Q1 13 8 13 M39 21 Q39 13 32 13" fill="none" stroke="#1d4a2a" stroke-width="1.4"/>
    </svg>
    <div class="step-text step-text--sm" style="left:186px;top:492px">Arrive at<br>home</div>

    <!-- running late -->
    <span class="num" style="left:272px;top:255px;font-size:44px">1</span>
    <span class="divider" style="left:302px;top:258px;height:38px"></span>
    <svg class="icon" style="left:316px;top:247px" width="36" height="32" viewBox="0 0 36 32" aria-hidden="true">
      <path d="M2 14 L18 6 L34 14" fill="none" stroke="#1d4a2a" stroke-width="1.4"/>
      <rect x="3" y="14" width="30" height="17" fill="none" stroke="#1d4a2a" stroke-width="1.4"/>
      <line x1="18" y1="6" x2="18" y2="0" stroke="#1d4a2a" stroke-width="1.2"/>
      <rect x="18" y="0" width="5" height="3" fill="#1d4a2a"/>
      <circle cx="18" cy="13" r="2.5" fill="none" stroke="#f5c400" stroke-width="1.2"/>
      <rect x="15" y="23" width="6" height="8" fill="none" stroke="#1d4a2a" stroke-width="1.2"/>
      <rect x="6" y="18" width="5" height="4" fill="none" stroke="#1d4a2a"/><rect x="25" y="18" width="5" height="4" fill="none" stroke="#1d4a2a"/>
    </svg>
    <div class="step-text step-text--sm" style="left:311px;top:286px">Sign in at<br>Student<br>Service</div>
    <span class="connector" style="left:301px;top:317px;height:21px"></span>

    <span class="num" style="left:272px;top:357px;font-size:44px">2</span>
    <span class="divider" style="left:302px;top:360px;height:38px"></span>
    <svg class="icon lockers" style="left:319px;top:351px" width="36" height="30" viewBox="0 0 36 30" aria-hidden="true">
      <rect x="1" y="1" width="34" height="28" fill="none" stroke="#1d4a2a" stroke-width="1.4"/>
      <line x1="18" y1="1" x2="18" y2="29" stroke="#1d4a2a" stroke-width="1.2"/>
      <line x1="1" y1="14" x2="35" y2="14" stroke="#1d4a2a" stroke-width="1.2"/>
      <rect x="22" y="18" width="9" height="8" fill="none" stroke="#1d4a2a" stroke-width="1.2"/>
      <circle cx="6" cy="19" r="1.5" fill="#f5c400"/><circle cx="6" cy="6" r="1.5" fill="#f5c400"/>
    </svg>
    <div class="step-text step-text--sm" style="left:311px;top:386px">Place bag<br>in locker</div>
    <span class="connector" style="left:301px;top:421px;height:21px"></span>

    <span class="num" style="left:272px;top:461px;font-size:44px">3</span>
    <span class="divider" style="left:302px;top:464px;height:38px"></span>
    <svg class="icon" style="left:320px;top:454px" width="24" height="34" viewBox="0 0 24 34" aria-hidden="true">
      <rect x="2" y="1" width="20" height="32" fill="none" stroke="#1d4a2a" stroke-width="1.4"/>
      <rect x="5" y="4" width="14" height="29" fill="none" stroke="#1d4a2a" stroke-width="1"/>
      <circle cx="8" cy="19" r="1.5" fill="#f5c400"/>
    </svg>
    <div class="step-text step-text--sm" style="left:311px;top:492px">Prompt<br>Arrival</div>

    <div class="footer" style="width:190px"><div class="footer-value">INTEGRITY</div><div class="footer-sub">WENDALE LEARNER VALUES</div></div>
  </section>

</div>
</body>
</html>
```